Election features for a political website

The Hearthside Ledger (www.hearthsideledger.example)
Web banner designs
Please have a look at The Hearthside Ledger website (www.hearthsideledger.example). We are seeking to add an advertising style banner at the top of every page and post. It will run right across the page (1024 pixels) and be in the region of 200 pixels vertically. (Please advise on what looks best size wise.
The banner will be a slider, operated in a similar way to the current homepage slider. There will be four items on the slider, and so we need four designs that match the aesthetic feel of the website. Each slider will link through to posts on the website.
1.
Headline: OUR CANDIDATE OF THE DAY
Space for a name, head and shoulders picture of the person to be dropped in and a one line reason. This will need to be in an editable format as this image will be changed each day for one month.
2.
Headline: HERO OF THE DAY
Space for name and a one line reason. This will need to be in an editable format as this image will be changed each day for one month.
3.
Headline: VILLAIN OF THE DAY
Space for name of the person to be dropped in and a one line reason. This will need to be in an editable format as this image will be changed each day for one month.
4.
Headline: THL Poll – [Date]
If the election was today, who would you vote for?
Clickable options:
Brightfolders
Ashvel
Marden Alliancers
Vornu
Tally
Other
Can a poll widget be added to the banner? We would like this poll to reset each day and then pool the results into a graph day by day over a one month period.
Reason: Payment is now guaranteed. We would like to see more options.

```html
<!DOCTYPE html>
<html lang="en">
<head>
<meta charset="utf-8">
<title>Our Candidate of the Day – Banner</title>
<link rel="stylesheet" href="https://fonts.googleapis.com/css2?family=Open+Sans:wght@300;400;700&display=swap">
<style>
  :root {
    --page-bg: #f2f2f2;
    --navy-deep: #16205a;
    --navy: #25357e;
    --royal: #3a56b8;
    --sky: #4f86dc;
    --pale-blue: #a9c1ec;
    --white: #ffffff;
    --ribbon-light: #ffc21a;
    --ribbon-dark: #f7931e;
    --portrait-top: #6b4a33;
    --portrait-bottom: #3f8fb8;
  }
  html, body {
    margin: 0;
    width: 1200px;
    height: 800px;
    overflow: hidden;
    background: var(--page-bg);
    font-family: "Open Sans", Arial, sans-serif;
  }
  .banner {
    position: absolute;
    left: 90px;
    top: 179px;
    width: 1024px;
    height: 348px;
    overflow: hidden;
    color: var(--white);
  }
  .banner__backdrop {
    position: absolute;
    inset: 0;
  }
  .headline {
    position: absolute;
    left: 108px;
    top: 112px;
    margin: 0;
    font-weight: 300;
    line-height: 1;
    letter-spacing: -1px;
  }
  .headline__our { font-size: 54px; font-weight: 300; }
  .headline__candidate { font-size: 54px; font-weight: 700; letter-spacing: -1.5px; }
  .headline__line2 {
    display: block;
    margin-left: 70px;
    margin-top: -6px;
  }
  .headline__of-the { font-size: 28px; font-weight: 300; letter-spacing: -0.5px; }
  .headline__day { font-size: 50px; font-weight: 300; }
  .portrait {
    position: absolute;
    left: 658px;
    top: 46px;
    width: 174px;
    height: 170px;
    border-radius: 70px 70px 30px 30px;
    background: linear-gradient(180deg, var(--portrait-top) 0%, #a98a74 40%, var(--portrait-bottom) 75%);
    opacity: 0.9;
  }
  .name-ribbon {
    position: absolute;
    left: 616px;
    top: 214px;
    width: 256px;
    height: 38px;
  }
  .name-ribbon__label {
    position: absolute;
    inset: 0;
    display: flex;
    align-items: center;
    justify-content: center;
    font-size: 17px;
    font-weight: 700;
    letter-spacing: -0.3px;
  }
  .candidate-reason {
    position: absolute;
    left: 543px;
    top: 259px;
    width: 400px;
    margin: 0;
    text-align: center;
    font-size: 12.5px;
    letter-spacing: -0.3px;
  }
</style>
</head>
<body>
<section class="banner">
  <svg class="banner__backdrop" viewBox="0 0 1024 348" width="1024" height="348" aria-hidden="true">
    <defs>
      <linearGradient id="sky-fill" x1="0" y1="0" x2="1" y2="1">
        <stop offset="0" stop-color="#2a3d8a"/>
        <stop offset="0.45" stop-color="#2f4596"/>
        <stop offset="0.7" stop-color="#2a3c8c"/>
        <stop offset="1" stop-color="#4a7fd8"/>
      </linearGradient>
      <linearGradient id="top-shade" x1="1" y1="0" x2="0.4" y2="0.6">
        <stop offset="0" stop-color="#141d52" stop-opacity="0.9"/>
        <stop offset="1" stop-color="#141d52" stop-opacity="0"/>
      </linearGradient>
      <linearGradient id="swoosh-white" x1="0" y1="0" x2="1" y2="0">
        <stop offset="0" stop-color="#eef2fb"/>
        <stop offset="0.5" stop-color="#ffffff"/>
        <stop offset="1" stop-color="#d8e4f8"/>
      </linearGradient>
    </defs>
    <rect width="1024" height="348" fill="url(#sky-fill)"/>
    <rect width="1024" height="348" fill="url(#top-shade)"/>
    <path d="M0,205 C260,245 520,300 1024,318 L1024,348 L0,348 Z" fill="#1d2a6a"/>
    <path d="M0,218 C260,256 520,318 1024,334 L1024,348 L0,348 Z" fill="url(#swoosh-white)"/>
    <path d="M0,300 C200,320 450,342 1024,336 L1024,348 L0,348 Z" fill="#3457b0"/>
    <path d="M0,318 C250,334 500,346 1024,342 L1024,348 L0,348 Z" fill="var(--pale-blue)"/>
  </svg>

  <h1 class="headline">
    <span class="headline__our">Our</span>
    <span class="headline__candidate">Candidate</span>
    <span class="headline__line2"><span class="headline__of-the">of the</span><span class="headline__day">Day</span></span>
  </h1>

  <div class="portrait" role="img" aria-label="Head and shoulders photo of the candidate of the day"></div>

  <div class="name-ribbon">
    <svg viewBox="0 0 256 38" width="256" height="38" aria-hidden="true">
      <defs>
        <linearGradient id="ribbon-fill" x1="0" y1="0" x2="1" y2="0">
          <stop offset="0" stop-color="var(--ribbon-dark)"/>
          <stop offset="0.5" stop-color="var(--ribbon-light)"/>
          <stop offset="1" stop-color="var(--ribbon-dark)"/>
        </linearGradient>
      </defs>
      <path d="M0,0 H256 L236,19 L256,38 H0 L20,19 Z" fill="url(#ribbon-fill)"/>
    </svg>
    <span class="name-ribbon__label">John Doe</span>
  </div>

  <p class="candidate-reason">This will need to be in an editable format as this image</p>
</section>
</body>
</html>
```